Book cover for ebook and Physical book for Mind Clutter Collective

I run a non-profit Mind Clutter Collective and I have a new book that needs a cover. For the physical book, I will need a full wrap. The mission is to help individuals Quiet the cycle of restless worry patterns. This book is title is "Quiet the cycle of restless worry patterns", and subtitle "Clear Your Mind of Static Noise." I am open to anything design wise, nothing is set in stone. Oh, MCC is pending Trademark.

Target Market(s)

Typically it's Mom's from 25-40

Industry/Entity Type

Mental Health

Font styles to use
Serif

Colors
f37122
9bcb3b
fbed22
0255a3
e34197

Requirements
Must have
• I do like simplicity, yet vibrant colors.
Nice to have
• The authors are Rex T. Whitford, and Dana Okonkwo. For some inspiration individuals refer to me as the Wonder Guide having reversed five incurable diseases.
Should not have
• The cover shouldn't be too busy.

```html
<!DOCTYPE html>
<html lang="en">
<head>
<meta charset="utf-8">
<title>Quiet the Cycle of Restless Worry Patterns — Book Cover</title>
<link rel="stylesheet" href="https://fonts.googleapis.com/css2?family=Abril+Fatface&family=Oswald:wght@500;600&display=swap">
<style>
  :root {
    --backdrop: #d9d6d1;
    --paper: #ece9e3;
    --paper-shade: #e2ded7;
    --spine: #1f3a6b;
    --navy-text: #2f4d7e;
    --rule: #7fb6dc;
    --tagline: #b0307a;
    --author: #5a6273;
    --blue: #0255a3;
    --orange: #f37122;
    --pink: #e34197;
    --yellow: #f6a81c;
    --green: #3d8f2e;
    --lime: #9bcb3b;
    --sun: #fbed22;
  }
  * { margin: 0; padding: 0; box-sizing: border-box; }
  html, body {
    width: 1200px;
    height: 796px;
    overflow: hidden;
    background: var(--backdrop);
  }
  .canvas {
    width: 1200px;
    height: 796px;
    display: flex;
    align-items: center;
    justify-content: center;
  }
  .cover {
    position: relative;
    width: 542px;
    height: 700px;
    background: linear-gradient(160deg, var(--paper) 0%, var(--paper-shade) 100%);
    box-shadow: 0 6px 22px rgba(0, 0, 0, 0.18);
    text-align: center;
  }
  .cover__spine {
    position: absolute;
    left: 0;
    top: 0;
    bottom: 0;
    width: 7px;
    background: var(--spine);
  }
  .title {
    position: absolute;
    top: 36px;
    left: 0;
    right: 0;
  }
  .title__word {
    display: block;
    font-family: "Abril Fatface", serif;
    font-size: 124px;
    line-height: 1;
    letter-spacing: 2px;
  }
  .title__word .c1 { color: var(--blue); }
  .title__word .c2 { color: var(--orange); }
  .title__word .c3 { color: var(--pink); }
  .title__word .c4 { color: var(--yellow); }
  .title__word .c5 { color: var(--green); }
  .title__rest {
    display: block;
    margin-top: 26px;
    font-family: "Oswald", sans-serif;
    font-weight: 600;
    font-size: 36px;
    line-height: 1.08;
    color: var(--navy-text);
    letter-spacing: 0.5px;
  }
  .rule {
    position: absolute;
    top: 278px;
    left: 70px;
    right: 30px;
    height: 2px;
    background: var(--rule);
  }
  .tagline {
    position: absolute;
    top: 290px;
    left: 0;
    right: 0;
    font-family: "Oswald", sans-serif;
    font-weight: 500;
    font-size: 21px;
    letter-spacing: 1.5px;
    color: var(--tagline);
  }
  .emblem {
    position: absolute;
    top: 560px;
    left: 50%;
    width: 88px;
    height: 66px;
    margin-left: -44px;
    border-radius: 50% 50% 45% 45%;
    background: radial-gradient(circle at 30% 40%, var(--pink) 0%, transparent 45%),
                radial-gradient(circle at 70% 35%, var(--lime) 0%, transparent 45%),
                radial-gradient(circle at 50% 75%, var(--sun) 0%, transparent 50%),
                linear-gradient(120deg, var(--blue), var(--orange));
    opacity: 0.85;
  }
  .authors {
    position: absolute;
    top: 676px;
    left: 0;
    right: 0;
    font-family: "Oswald", sans-serif;
    font-weight: 500;
    font-size: 12px;
    letter-spacing: 2.5px;
    color: var(--author);
  }
</style>
</head>
<body>
  <main class="canvas">
    <section class="cover">
      <div class="cover__spine"></div>
      <h1 class="title">
        <span class="title__word"><span class="c1">Q</span><span class="c2">U</span><span class="c3">I</span><span class="c4">E</span><span class="c5">T</span></span>
        <span class="title__rest">THE CYCLE OF RESTLESS<br>WORRY PATTERNS</span>
      </h1>
      <div class="rule"></div>
      <p class="tagline">CLEAR YOUR MIND OF STATIC NOISE</p>
      <div class="emblem" role="img" aria-label="Small multicoloured brain illustration"></div>
      <p class="authors">REX T. WHITFORD &amp; DANA OKONKWO</p>
    </section>
  </main>
</body>
</html>
```